Email signature design - law firm

We are a small boutique law firm which is located near the beach in Manly, Australia.

We have just recently developed a new logo and are looking to redesign our letterhead, business cards and email signatures.

This brief is for our email signatures. This is an email signature to appear at the bottom of our Outlook emails so we would like it to be text that we are able to edit as the wording in our email signature often required amendments.

I have attached a word document which had our new logo, and our previous email signature which all the information/wording that needs to be included.

We would like multiple designs with a modern, simplistic yet striking look.

Thanks.

font - raleway or montserrat
Updates

Colors

Designer to choose colors to be used in the design.

Requirements
Must have
• Must have the exact wording which appears in the email signature in the word document attached to brief.
• Must be able to edit the text as it is for an Outlook email signature which wording will change from time to time.

```html
<!DOCTYPE html>
<html lang="en">
<head>
<meta charset="utf-8">
<title>Email Signature – Corlett &amp; Vance</title>
<link rel="stylesheet" href="https://fonts.googleapis.com/css2?family=Raleway:wght@400;500;700&display=swap">
<style>
  :root {
    --ink: #222222;
    --rule: #444444;
    --navy: #2e4290;
    --gold: #c9ad63;
    --paper: #ffffff;
  }
  html, body {
    margin: 0;
    padding: 0;
    overflow: hidden;
    background: var(--paper);
  }
  .canvas {
    position: relative;
    width: 1200px;
    height: 1000px;
    overflow: hidden;
    background: var(--paper);
    font-family: "Raleway", sans-serif;
    color: var(--ink);
  }
  .sign-off {
    position: absolute;
    left: 95px;
    top: 181px;
    margin: 0;
    font-size: 21px;
    font-weight: 400;
  }
  .signer-name {
    position: absolute;
    left: 95px;
    top: 222px;
    margin: 0;
    font-size: 21px;
    font-weight: 700;
  }
  .rule {
    position: absolute;
    left: 95px;
    height: 1px;
    background: var(--rule);
  }
  .rule--top { top: 295px; width: 651px; }
  .rule--bottom { top: 478px; width: 1005px; }
  .firm-mark {
    position: absolute;
    left: 95px;
    top: 312px;
    width: 240px;
    height: 148px;
    display: flex;
    align-items: center;
    gap: 12px;
  }
  .firm-mark__dot {
    width: 22px;
    height: 22px;
    border-radius: 50%;
    background: var(--navy);
    flex: none;
  }
  .firm-mark__name {
    font-size: 22px;
    font-weight: 700;
    color: var(--navy);
    letter-spacing: 0.5px;
  }
  .divider {
    position: absolute;
    left: 350px;
    top: 312px;
    width: 4px;
    height: 153px;
    background: linear-gradient(to bottom, rgba(201,173,99,0) 0%, var(--gold) 45%, rgba(201,173,99,0) 100%);
  }
  .contact {
    position: absolute;
    left: 379px;
    top: 321px;
    margin: 0;
    font-style: normal;
    font-size: 22px;
    line-height: 26.6px;
    font-weight: 400;
  }
  .contact__sep { color: var(--navy); }
  .disclaimer {
    position: absolute;
    left: 95px;
    top: 505px;
    width: 1010px;
    font-size: 17.6px;
    line-height: 20.5px;
    text-align: justify;
  }
  .disclaimer p { margin: 0; }
  .disclaimer .gap { margin-top: 20.5px; }
</style>
</head>
<body>
<main class="canvas">
  <p class="sign-off">Regards</p>
  <p class="signer-name">Maren Ellison</p>

  <div class="rule rule--top"></div>

  <div class="firm-mark">
    <span class="firm-mark__dot"></span>
    <span class="firm-mark__name">Corlett &amp; Vance</span>
  </div>

  <div class="divider"></div>

  <address class="contact">
    Suite 4 <span class="contact__sep">|</span> 18 Ocean Crest Lane<br>
    SEAHAVEN NSW 2199<br>
    T: (02) 5550 1842<br>
    F: (02) 5550 1843<br>
    www.corlettvance.com.au
  </address>

  <div class="rule rule--bottom"></div>

  <section class="disclaimer">
    <p>Important note: This E-Mail and any attachment is PRIVILEGED and confidential.&nbsp; It must not be read, copied, disclosed or used by any person other than the above named addressees.&nbsp; In order to preserve the intended confidentiality and privilege, please notify us immediately if you have received this e-mail by mistake and secure-delete this e-mail from your system.</p>
    <p>Unauthorised perusal, use, disclosure, forwarding or copying is strictly prohibited and may be unlawful.</p>
    <p class="gap">Liability limited by a scheme approved under Professional Standards Legislation. Legal practitioners at CoastLegal (NSW) Pty Ltd are members of the scheme.</p>
    <p class="gap">Fraud warning: Please be aware that there is a significant risk posed by cyber fraud, specifically relating to email accounts and bank account details. Our bank account details will never change during the course of a transaction, and we will never advise you of a change to our bank details via email.&nbsp; Please check account details with us in person or by phone before making payments.&nbsp; If you advise us of your bank account details by email, please also ring and confirm the bank account details by phone as well.</p>
  </section>
</main>
</body>
</html>
```